Webdesign für Kfz-Betrieb
Zielgruppe
Seit über 20 Jahren ist Radwerk Olbertz die erste Anlaufstelle wenn es um die Themen Reifen, Felgen und den gesamten Kfz-Bereich geht. Außerdem ist das Unternehmen seit 1997 auf Fahrzeugaufbereitung spezialisiert.
ZG: Alle, die Reifen benötigen
Aufgabenstellung
Layout Adobe Photoshop
hell, freundlich, aufgeschlossen
Die Leistungen sollen mit Icons dargestellt werden. (siehe Welche Inhalte sollen angezeigt werden)
Logo liegt noch nicht vor
nur die Startseite layouten

```html
<!DOCTYPE html>
<html lang="de">
<head>
<meta charset="utf-8">
<title>Radwerk Olbertz – Startseite</title>
<link rel="stylesheet" href="https://fonts.googleapis.com/css2?family=Noto+Sans:wght@400;600;700;800&display=swap">
<style>
  :root {
    --brand-green: #14991a;
    --brand-red: #e30613;
    --ink: #111111;
    --white: #ffffff;
    --hero-dark: #141414;
    --hero-mid: #3a3a3a;
  }
  * { box-sizing: border-box; margin: 0; padding: 0; }
  html, body {
    width: 1200px; height: 798px; overflow: hidden;
    font-family: "Noto Sans", sans-serif; color: var(--ink); background: var(--white);
  }
  .page { position: relative; width: 1200px; height: 798px; }

  .site-header { position: absolute; top: 0; left: 0; width: 1200px; height: 157px; background: var(--white); }
  .brand {
    position: absolute; left: 163px; top: 78px;
    display: flex; align-items: center; gap: 10px;
  }
  .brand-dot { width: 26px; height: 26px; border-radius: 50%; background: var(--brand-red); }
  .brand-name { font-size: 31px; font-weight: 800; color: var(--brand-green); letter-spacing: -0.5px; }

  .main-nav { position: absolute; left: 499px; top: 26px; width: 540px; }
  .nav-row { display: flex; gap: 13px; list-style: none; }
  .nav-row + .nav-row { margin-top: 18px; gap: 16px; }
  .nav-item { display: flex; flex-direction: column; align-items: center; gap: 3px; font-size: 15px; white-space: nowrap; }
  .nav-item svg { width: 28px; height: 26px; stroke: var(--ink); fill: none; stroke-width: 1.4; stroke-linecap: round; stroke-linejoin: round; }

  .hero {
    position: absolute; top: 157px; left: 0; width: 1200px; height: 578px;
    background:
      radial-gradient(ellipse 60% 70% at 45% 55%, var(--hero-mid), transparent 75%),
      linear-gradient(120deg, #262626 0%, var(--hero-dark) 60%, #0a0a0a 100%);
  }
  .hero-content { position: absolute; left: 163px; top: 118px; width: 540px; color: var(--white); }
  .hero-title { font-size: 33px; font-weight: 700; line-height: 43px; }
  .hero-text { margin-top: 22px; font-size: 20px; line-height: 30px; }
  .hero-button {
    display: inline-block; margin-top: 26px; padding: 0 20px; height: 32px; line-height: 32px;
    border-radius: 16px; background: var(--brand-red); color: var(--white);
    font-size: 16px; font-weight: 500; text-decoration: none;
  }

  .site-footer {
    position: absolute; bottom: 0; left: 0; width: 1200px; height: 63px; background: var(--brand-green);
    display: flex; justify-content: flex-end; align-items: center; gap: 25px; padding-right: 175px;
  }
  .site-footer a { color: var(--white); font-size: 16px; text-decoration: none; }
</style>
</head>
<body>
<div class="page">
  <header class="site-header">
    <div class="brand">
      <span class="brand-dot"></span>
      <span class="brand-name">Radwerk Olbertz</span>
    </div>
    <nav class="main-nav">
      <ul class="nav-row">
        <li class="nav-item">
          <svg viewBox="0 0 28 26"><path d="M14 6 C10 3 6 3 3 4 V23 C6 22 10 22 14 25 C18 22 22 22 25 23 V4 C22 3 18 3 14 6 Z M14 6 V25"/></svg>
          Leistungen
        </li>
        <li class="nav-item">
          <svg viewBox="0 0 28 26"><circle cx="14" cy="14" r="10"/><path d="M14 8 V14 L18 11 M12 3 H16"/></svg>
          Terminvereinbarung
        </li>
        <li class="nav-item">
          <svg viewBox="0 0 40 26"><rect x="2" y="7" width="36" height="16"/><path d="M2 12 H38 M7 7 V3 H17 V7 M23 7 V3 H33 V7 M6 16 V20 M9 16 V20 M12 16 V20 M26 16 V20 M29 16 V20 M32 16 V20"/></svg>
          Unternehmen
        </li>
        <li class="nav-item">
          <svg viewBox="0 0 28 26"><circle cx="14" cy="13" r="11"/><path d="M14 7 V15"/><circle cx="14" cy="19" r="0.8"/></svg>
          Aktuelles
        </li>
        <li class="nav-item">
          <svg viewBox="0 0 28 26"><path d="M16 3 H24 V11 L12 23 L4 15 Z"/><circle cx="20" cy="7" r="1.5"/></svg>
          Abverkauf
        </li>
      </ul>
      <ul class="nav-row">
        <li class="nav-item">
          <svg viewBox="0 0 28 26"><circle cx="14" cy="13" r="4"/><path d="M14 2 L16 5 L19.5 4 L20 7.5 L23.5 8.5 L22 12 L24 15 L21 16.5 L21 20 L17.5 20 L15.5 23.5 L13 21 L10 23 L8.5 19.5 L5 19 L5.5 15.5 L3 13 L5.5 10.5 L5 7 L8.5 6.5 L10 3 L13 5 Z"/></svg>
          Reifenkonfigurator von reifenwahl24.de
        </li>
        <li class="nav-item">
          <svg viewBox="0 0 40 26"><path d="M2 12 H10 L18 8 C22 7 26 8 28 10 L36 7 C38 7 38 9 37 10 L26 18 H12 L2 20 M20 13 H27"/></svg>
          Engagement
        </li>
      </ul>
    </nav>
  </header>

  <section class="hero" role="img" aria-label="Nahaufnahme eines dunklen Autoreifens mit Profil">
    <div class="hero-content">
      <h1 class="hero-title">Wir sind Ihr Ansprechpartner, wenn es um Reifen geht!</h1>
      <p class="hero-text">Seit über 20 Jahren ist Radwerk Olbertz die erste Anlaufstelle, wenn es um die Themen Reifen, Felgen und den gesamten Kfz-Bereich geht.</p>
      <a class="hero-button" href="#">Mehr erfahren</a>
    </div>
  </section>

  <footer class="site-footer">
    <a href="#">Datenschutz</a>
    <a href="#">Impressum</a>
  </footer>
</div>
</body>
</html>
```